Manufacturing company needs new business card.

I need a unique Business Card that will truly stand out. Nothing too busy. Simple is good, right? Not looking for a standard design either. No cookie cutter layout. I am just looking for something interesting and a bit different. Does't have to completely off the wall crazy, just not your run of the mill business card. Clean and modern with a touch of industrial.

Target Market(s)

Air conditioning industry, Architects, builders.

Industry/Entity Type

Business

Contact Information for Business Card

Details to be included on card are:

Peter Vance
Managing Director

T: 1300 847 519
M: 0428 593 174
W: www.brenvaleworks.com.au
E: peter.vance@brenvaleworks.com.au
A: 58 Harwick Lane, Sydney NSW 2000

Font styles to use
Sans Serif

Colors
0355a3
848484
fbfbfb

Requirements
Must have
• Card design must be landscape.

```html
<!DOCTYPE html>
<html lang="en">
<head>
<meta charset="utf-8">
<title>Brenvale Works – Business Card</title>
<link rel="stylesheet" href="https://fonts.googleapis.com/css2?family=Lato:wght@400;700&display=swap">
<style>
  :root {
    --brand-blue: #1f4fa8;
    --brand-grey: #848484;
    --card-white: #fbfbfb;
    --card-black: #262626;
    --backdrop: #d9d9d9;
  }
  * { margin: 0; padding: 0; box-sizing: border-box; }
  html, body { width: 1200px; height: 900px; overflow: hidden; }
  body {
    background: var(--backdrop);
    font-family: "Lato", Arial, sans-serif;
    position: relative;
  }
  .card {
    position: absolute;
    width: 620px;
    height: 354px;
    box-shadow: 0 10px 28px rgba(0,0,0,0.25);
  }
  .card-back {
    left: 520px; top: 60px;
    background: var(--card-black);
    display: flex; align-items: center; justify-content: center;
  }
  .card-front {
    left: 60px; top: 470px;
    background: var(--card-white);
  }
  .wordmark {
    display: flex; align-items: center; gap: 14px;
    font-weight: 700; font-size: 30px; letter-spacing: 0.5px;
  }
  .wordmark-square { width: 30px; height: 30px; }
  .card-back .wordmark { color: var(--card-white); }
  .card-back .wordmark-square { background: var(--card-white); }
  .card-front .wordmark {
    position: absolute; left: 48px; top: 44px;
    color: var(--brand-blue);
  }
  .card-front .wordmark-square { background: var(--brand-blue); }
  .contact-list {
    position: absolute; left: 48px; top: 132px;
    list-style: none;
  }
  .contact-item {
    display: flex; align-items: center; gap: 12px;
    color: var(--brand-blue); font-size: 15px; line-height: 24px;
  }
  .contact-icon { width: 14px; height: 14px; flex: none; }
  .contact-icon * { fill: none; stroke: var(--brand-grey); stroke-width: 1.6; }
  .contact-person {
    position: absolute; right: 70px; top: 212px;
  }
  .person-name {
    color: var(--brand-blue); font-weight: 700; font-size: 22px; letter-spacing: 0.5px;
  }
  .person-title { color: var(--brand-grey); font-size: 15px; }
  .address-band {
    position: absolute; left: 0; right: 0; top: 272px; height: 42px;
    background: var(--brand-blue);
    color: var(--card-white); font-size: 15px;
    display: flex; align-items: center; padding-left: 110px;
  }
</style>
</head>
<body>
  <section class="card card-back">
    <div class="wordmark"><span class="wordmark-square"></span><span>Brenvale Works</span></div>
  </section>

  <section class="card card-front">
    <div class="wordmark"><span class="wordmark-square"></span><span>Brenvale Works</span></div>

    <ul class="contact-list">
      <li class="contact-item">
        <svg class="contact-icon" viewBox="0 0 14 14"><rect x="3" y="1" width="8" height="12" rx="1.5"/></svg>
        <span>0428 593 174</span>
      </li>
      <li class="contact-item">
        <svg class="contact-icon" viewBox="0 0 14 14"><path d="M3 1.5 L5.5 1.5 L6.5 4.5 L5 5.8 C5.8 7.6 6.6 8.4 8.2 9 L9.5 7.5 L12.5 8.5 L12.5 11 C12.5 12 11.5 12.8 10.5 12.5 C6 11.5 2.5 8 1.5 3.5 C1.3 2.5 2 1.5 3 1.5 Z"/></svg>
        <span>1300 847 519</span>
      </li>
      <li class="contact-item">
        <svg class="contact-icon" viewBox="0 0 14 14"><rect x="1" y="3" width="12" height="8"/><path d="M1 3 L7 8 L13 3"/></svg>
        <span>peter.vance@brenvaleworks.com.au</span>
      </li>
      <li class="contact-item">
        <svg class="contact-icon" viewBox="0 0 14 14"><circle cx="7" cy="7" r="5.8"/><ellipse cx="7" cy="7" rx="2.5" ry="5.8"/><path d="M1.2 7 H12.8"/></svg>
        <span>www.brenvaleworks.com.au</span>
      </li>
    </ul>

    <div class="contact-person">
      <div class="person-name">PETER VANCE</div>
      <div class="person-title">Managing Director</div>
    </div>

    <div class="address-band">58 Harwick Lane, Sydney NSW 2000</div>
  </section>
</body>
</html>
```